Needed Box Packaging: Dog XL Puppy Pee/Poo Pads

We're looking for a creative and fun design for our XL puppy pads. Attached is all the documents you will need.

Our pads are unique with Bamboo Charcoal and optional Adhesive sticker backing on the corners. 23" x 35" is the size. There's 50 per box.

ABSORBS 2x as much, 2x as fast, so you never come home to ruined floors
BLACK puppy pads, so your pets mess stays discrete and you never see a yellow stain on a white puppy pad in your home
ODOR ELIMINATION with carbon technology for all-day use to ensure your home stays fresh
LEAK PROOF Sorbix Polymer turns liquid into gel instantly to guarantee dry floors and easy clean up
PHEROMONE ATTRACTION to ensure pets feel comfortable and knows to hit the right spot every time

Target Market(s)

Dog owners

Font styles to use
Sans Serif

Colors
33a6d7
33b8a4
acd036
fbee3d
faa54b

Requirements
Must have
• Must have logo, size of pads, benefits, UPC code, number packed per box, pictures of a dog and picture of the pads
Should not have
• cats

```html
<!DOCTYPE html>
<html lang="en">
<head>
<meta charset="utf-8">
<title>XL Puppy Training Pads – Box Front</title>
<link rel="stylesheet" href="https://fonts.googleapis.com/css2?family=Arvo:wght@700&family=Barlow+Condensed:wght@600;700;800&family=Barlow:wght@400&display=swap">
<style>
  :root {
    --scene-light: #eee6d6;
    --scene-mid: #d8cfb8;
    --scene-green: #b9d84a;
    --scene-yellow: #d9d45a;
    --ink: #1e1f1d;
    --white: #ffffff;
    --band: #f6b81c;
    --pad-dark: #2a2d2c;
    --pad-edge: #e9ecef;
    --dog-tan: #dcb272;
    --dog-light: #f0d9a8;
  }
  * { margin: 0; padding: 0; box-sizing: border-box; }
  html, body { width: 1200px; height: 910px; overflow: hidden; background: var(--white); }
  .box-front { position: relative; width: 1200px; height: 910px; overflow: hidden; }

  .scene-photo {
    position: absolute; inset: 0;
    background:
      radial-gradient(ellipse 300px 260px at 420px 330px, var(--scene-yellow), transparent 70%),
      radial-gradient(ellipse 420px 380px at 1020px 260px, var(--scene-green), transparent 75%),
      linear-gradient(180deg, var(--scene-light) 0%, var(--scene-mid) 70%, #cfc4aa 100%);
  }
  .pad-photo {
    position: absolute; left: 484px; top: 552px; width: 716px; height: 284px;
    background: linear-gradient(160deg, var(--pad-edge) 0 6%, var(--pad-dark) 12%, #3a3e3d 100%);
    clip-path: polygon(30% 0, 100% 0, 100% 100%, 0 100%, 4% 70%);
  }
  .dog-photo {
    position: absolute; left: 736px; top: 92px; width: 464px; height: 744px;
    background: radial-gradient(ellipse at 45% 55%, var(--dog-light), var(--dog-tan) 70%);
    border-radius: 48% 48% 30% 30% / 30% 30% 20% 20%;
  }

  .brand-name {
    position: absolute; left: 922px; top: 36px;
    font: 700 34px "Barlow Condensed", sans-serif; color: var(--ink); letter-spacing: 0.5px;
  }

  .title { position: absolute; left: 66px; font-family: "Arvo", serif; font-weight: 700; line-height: 1; }
  .title-size { top: 92px; font-size: 92px; color: var(--ink); }
  .title-main { top: 184px; font-size: 166px; color: var(--white); letter-spacing: -2px; }
  .title-sub { top: 339px; font-size: 76px; color: var(--white); letter-spacing: -1px; }

  .deco-paw { position: absolute; width: 60px; height: 60px; }

  .benefits { position: absolute; left: 66px; top: 436px; list-style: none; }
  .benefit { position: relative; padding-left: 70px; height: 80px; width: 420px; }
  .benefit .paw { position: absolute; left: 0; top: 4px; width: 58px; height: 58px; }
  .benefit h3 { font: 700 26px "Barlow Condensed", sans-serif; color: var(--ink); line-height: 1; }
  .benefit h3 span { font-size: 22px; }
  .benefit p { font: 400 13.5px/1.2 "Barlow", sans-serif; color: var(--ink); text-align: justify; width: 342px; margin-top: 3px; }

  .bottom-band {
    position: absolute; left: 0; bottom: 0; width: 1200px; height: 74px; background: var(--band);
  }
  .bottom-band p {
    position: absolute; left: 68px; top: 20px;
    font: 700 25px "Barlow Condensed", sans-serif; color: var(--white); letter-spacing: 0.2px;
  }
  .count-badge {
    position: absolute; left: 968px; top: 707px; width: 176px; height: 203px;
    background: var(--band); border-radius: 88px 88px 0 0; text-align: center; color: var(--white);
  }
  .count-number { font: 800 112px/1 "Barlow Condensed", sans-serif; margin-top: 10px; }
  .count-label { font: 700 30px/1 "Arvo", serif; margin-top: -4px; }
  .count-size { font: 700 25px/1 "Arvo", serif; }
</style>
</head>
<body>
<svg width="0" height="0" style="position:absolute">
  <defs>
    <symbol id="paw" viewBox="0 0 60 60">
      <ellipse cx="30" cy="42" rx="15" ry="12" fill="#fff"/>
      <ellipse cx="12" cy="26" rx="6" ry="8" fill="#fff"/>
      <ellipse cx="23" cy="14" rx="6" ry="8" fill="#fff"/>
      <ellipse cx="37" cy="14" rx="6" ry="8" fill="#fff"/>
      <ellipse cx="48" cy="26" rx="6" ry="8" fill="#fff"/>
    </symbol>
  </defs>
</svg>
<main class="box-front">
  <div class="scene-photo" role="img" aria-label="Softly blurred living room with yellow vases and a green sofa"></div>
  <div class="pad-photo" role="img" aria-label="Black training pad with white border laid on the floor"></div>
  <div class="dog-photo" role="img" aria-label="Golden retriever puppy sitting on the training pad"></div>

  <div class="brand-name">pawhaven</div>

  <h1>
    <span class="title title-size">XL</span>
    <span class="title title-main">PUPPY</span>
    <span class="title title-sub">TRAINING PADS</span>
  </h1>
  <svg class="deco-paw" style="left:585px;top:132px"><use href="#paw"/></svg>
  <svg class="deco-paw" style="left:638px;top:180px"><use href="#paw"/></svg>

  <ul class="benefits">
    <li class="benefit"><svg class="paw"><use href="#paw"/></svg>
      <h3>ABSORBS <span>2x as much, 2x as fast,</span></h3>
      <p>so you never come home to ruined floors</p></li>
    <li class="benefit"><svg class="paw"><use href="#paw"/></svg>
      <h3>BLACK <span>puppy pads</span></h3>
      <p>so your pets mess stays discrete and you never see a yellow stain on a white puppy pad in your home</p></li>
    <li class="benefit"><svg class="paw"><use href="#paw"/></svg>
      <h3>ODOR ELIMINATION</h3>
      <p>with carbon technology for all-day use to ensure your home stays fresh</p></li>
    <li class="benefit"><svg class="paw"><use href="#paw"/></svg>
      <h3>LEAK PROOF</h3>
      <p>Sorbix Polymer turns liquid into gel instantly to guarantee dry floors and easy clean up</p></li>
    <li class="benefit"><svg class="paw"><use href="#paw"/></svg>
      <h3>PHEROMONE ATTRACTION</h3>
      <p>to ensure pets feel comfortable and knows to hit the right spot every time</p></li>
  </ul>

  <div class="bottom-band"><p>BAMBOO CHARCOAL AND OPTIONAL ADHESIVE STICKER BACKING ON THE CORNERS</p></div>
  <div class="count-badge">
    <div class="count-number">50</div>
    <div class="count-label">PIECES</div>
    <div class="count-size">23” x 35”</div>
  </div>
</main>
</body>
</html>
```